Small consulting business needs logo and business card design

I need a logo, business card and letterhead design for a small consulting firm called Kestrawell Consulting. My customers are generally small to medium sized businesses but I have done work for major corporates and government departments. The field of consulting is strategic/business planning and program management. I have blue as the predominate colour in my current business card but I am happy to change this for the right design
Industry/Entity Type
Business

```html
<!DOCTYPE html>
<html lang="en">
<head>
<meta charset="utf-8">
<title>Kestrawell Consulting – Business Card</title>
<link rel="stylesheet" href="https://fonts.googleapis.com/css2?family=Michroma&display=swap">
<style>
  :root {
    --page-bg: #ece9e4;
    --card-dark: #343436;
    --gold-light: #f7d80a;
    --gold-deep: #e9a400;
    --silver-light: #f2f2f2;
    --silver-dark: #9a9a9a;
    --ink: #2a2a2a;
    --brand: #e8b21c;
  }
  html, body {
    margin: 0;
    width: 1200px;
    height: 870px;
    overflow: hidden;
    background: var(--page-bg);
  }
  .canvas {
    position: relative;
    width: 1200px;
    height: 870px;
  }
  .card {
    position: absolute;
    left: 100px;
    top: 150px;
    width: 1000px;
    height: 571px;
    border-radius: 4px;
    overflow: hidden;
    box-shadow: 0 10px 30px rgba(0,0,0,0.25);
    background: radial-gradient(ellipse at 62% 45%, var(--gold-light) 0%, #f3c300 40%, var(--gold-deep) 100%);
    font-family: "Michroma", sans-serif;
    color: var(--ink);
  }
  .card-shape {
    position: absolute;
    inset: 0;
  }
  .brand {
    position: absolute;
    left: 70px;
    top: 360px;
    color: var(--brand);
    font-size: 30px;
    line-height: 1.25;
    letter-spacing: 2px;
    text-transform: uppercase;
  }
  .contact {
    position: absolute;
    right: 60px;
    top: 50px;
    text-align: right;
  }
  .person-name {
    font-size: 24px;
    letter-spacing: 1px;
    margin: 0;
  }
  .person-title {
    font-size: 17px;
    margin: 8px 0 0;
  }
  .address {
    margin: 70px 0 0;
    font-size: 17px;
    line-height: 1.7;
    font-style: normal;
    padding-right: 30px;
  }
  .lines {
    list-style: none;
    margin: 30px 0 0;
    padding: 0;
    font-size: 16px;
  }
  .lines li {
    display: flex;
    justify-content: flex-end;
    align-items: center;
    gap: 10px;
    height: 36px;
  }
  .lines svg {
    width: 20px;
    height: 20px;
    fill: var(--ink);
  }
</style>
</head>
<body>
<main class="canvas">
  <section class="card" aria-label="Kestrawell Consulting business card">
    <svg class="card-shape" viewBox="0 0 1000 571" aria-hidden="true">
      <defs>
        <linearGradient id="silver" x1="0" y1="0" x2="1" y2="0">
          <stop offset="0" stop-color="var(--silver-dark)"/>
          <stop offset="0.5" stop-color="var(--silver-light)"/>
          <stop offset="1" stop-color="var(--silver-dark)"/>
        </linearGradient>
      </defs>
      <path d="M0,0 L330,0 C360,190 470,300 560,571 L0,571 Z" fill="url(#silver)"/>
      <path d="M0,0 L305,0 C330,200 445,310 530,571 L0,571 Z" fill="var(--card-dark)"/>
    </svg>

    <div class="brand">Kestrawell<br>Consulting</div>

    <div class="contact">
      <h1 class="person-name">DANIEL MARSH</h1>
      <p class="person-title">Managing Director</p>
      <address class="address">41 9th floor,Harbour<br>Row Road KLT</address>
      <ul class="lines">
        <li>012 555 0142
          <svg viewBox="0 0 20 20"><path d="M5 2l3 4-2 2c1 2 3 4 5 5l2-2 4 3-2 3C9 17 3 11 3 4z"/></svg>
        </li>
        <li>012 555 0142
          <svg viewBox="0 0 20 20"><path d="M6 1h8a1 1 0 0 1 1 1v16a1 1 0 0 1-1 1H6a1 1 0 0 1-1-1V2a1 1 0 0 1 1-1zm1 3v11h6V4z"/></svg>
        </li>
        <li>012 555 0142
          <svg viewBox="0 0 20 20"><path d="M6 2h7l2 2v4H6zM3 9h14a1 1 0 0 1 1 1v7H2v-7a1 1 0 0 1 1-1zm2 3v2h4v-2z"/></svg>
        </li>
        <li>hello@kestrawell.com
          <svg viewBox="0 0 20 20"><path d="M2 4h16v12H2zm1.5 1.5L10 11l6.5-5.5z"/></svg>
        </li>
        <li>www.kestrawell.com
          <svg viewBox="0 0 20 20"><path d="M10 1a9 9 0 1 0 0 18 9 9 0 0 0 0-18zm0 2c1.3 1.5 2 3.8 2.1 6H7.9C8 6.8 8.7 4.5 10 3zM3.1 9a7 7 0 0 1 3-5c-.9 1.5-1.4 3.2-1.5 5zm0 2h1.5c.1 1.8.6 3.5 1.5 5a7 7 0 0 1-3-5zm4.8 0h4.2c-.1 2.2-.8 4.5-2.1 6-1.3-1.5-2-3.8-2.1-6zm6 5c.9-1.5 1.4-3.2 1.5-5h1.5a7 7 0 0 1-3 5zm1.5-7c-.1-1.8-.6-3.5-1.5-5a7 7 0 0 1 3 5z"/></svg>
        </li>
      </ul>
    </div>
  </section>
</main>
</body>
</html>
```